Harbor Crew Biz Cards

looking for a new catchy business card where my cell number is very prominent:
My pic and logo are attached. My whole picture isn't necessary if it makes more sense to crop it.

Info needed:

(Big) Marcus Pellow
(Medium) Real Estate Professional
(Medium) Buyer/Seller Specialist
(Big) Call/Text 410-738-2914
(small) Marcuspell@quillbox.com
(small) www.harborcrewlists.com

(very small)
The Harbor Crew
at Keystead Real Estate
2457 W Tanbrook Rd, Bel Air, MD 21014
833-555-2690

```html
<!DOCTYPE html>
<html lang="en">
<head>
<meta charset="utf-8">
<title>Harbor Crew Business Cards</title>
<link href="https://fonts.googleapis.com/css2?family=Tinos:wght@400;700&display=swap" rel="stylesheet">
<style>
  :root {
    --navy: #1b2f5a;
    --navy-deep: #14244a;
    --white: #ffffff;
    --rule: #8d9ab8;
    --grey-text: #6e6e6e;
    --page: #e9e6e1;
    --suit: #2a3550;
    --shirt: #dfe3ee;
  }
  * { margin: 0; padding: 0; box-sizing: border-box; }
  html, body { width: 900px; height: 1200px; overflow: hidden; }
  body {
    background: var(--page);
    font-family: "Tinos", "Times New Roman", serif;
    position: relative;
  }
  .card {
    position: absolute;
    left: 82px;
    width: 735px;
    height: 427px;
    border-radius: 22px;
    overflow: hidden;
    box-shadow: 0 6px 14px rgba(0,0,0,0.25);
  }
  .card-front { top: 126px; background: var(--white); }
  .card-back { top: 638px; background: var(--navy); }

  .front-band {
    position: absolute; left: 0; top: 0;
    width: 100%; height: 262px;
    background: var(--navy);
  }
  .agent-info {
    position: absolute; left: 40px; top: 44px;
    color: var(--white);
  }
  .agent-name {
    font-weight: 700; font-size: 31px; letter-spacing: 1px;
    text-transform: uppercase; line-height: 1;
  }
  .agent-role {
    font-size: 19px; text-transform: uppercase; letter-spacing: 0.5px;
    line-height: 23px;
  }
  .agent-name + .agent-role { margin-top: 8px; }
  .info-rule {
    width: 345px; height: 1px; background: var(--rule);
    margin: 8px 0 12px;
  }
  .agent-phone {
    font-weight: 700; font-size: 27px; text-transform: uppercase; line-height: 1;
  }
  .agent-contact {
    font-size: 17px; line-height: 24px;
  }
  .agent-phone + .agent-contact { margin-top: 8px; }

  .office-info {
    position: absolute; left: 41px; top: 307px;
    color: var(--grey-text); font-size: 14px; line-height: 20.5px;
  }
  .office-name { text-transform: uppercase; letter-spacing: 0.3px; }
  .office-phone { display: flex; align-items: center; gap: 5px; }
  .office-phone svg { width: 10px; height: 10px; }

  .agent-photo {
    position: absolute; left: 403px; top: 14px;
    width: 292px; height: 413px;
    border-radius: 120px 120px 0 0;
    background: linear-gradient(180deg, #b78a74 0%, #a8846f 22%, var(--shirt) 30%, var(--suit) 45%, var(--suit) 100%);
  }

  .back-brand {
    position: absolute; left: 0; top: 0; width: 100%; height: 100%;
    display: flex; flex-direction: column; align-items: center; justify-content: center;
    color: var(--white); text-align: center;
  }
  .brand-mark {
    width: 120px; height: 120px; border-radius: 50%;
    border: 3px solid #9a9fa8; margin-bottom: 34px;
  }
  .brand-name {
    font-size: 40px; font-weight: 400; letter-spacing: 2px;
    text-transform: uppercase; line-height: 1.1;
  }
  .brand-sub {
    font-size: 15px; font-weight: 400; letter-spacing: 3px;
    text-transform: uppercase; margin-top: 10px;
  }
</style>
</head>
<body>
  <section class="card card-front">
    <div class="front-band"></div>
    <div class="agent-info">
      <h1 class="agent-name">Marcus Pellow</h1>
      <p class="agent-role">Real Estate Professional</p>
      <p class="agent-role">Buyer/Seller Specialist</p>
      <div class="info-rule"></div>
      <p class="agent-phone">Call/Text 410-738-2914</p>
      <p class="agent-contact">Marcuspell@quillbox.com</p>
      <p class="agent-contact">www.harborcrewlists.com</p>
    </div>
    <div class="office-info">
      <p class="office-name">The Harbor Crew</p>
      <p class="office-name">at Keystead Real Estate</p>
      <p>2457 W Tanbrook Rd, Bel Air, MD 21014</p>
      <p class="office-phone">
        <svg viewBox="0 0 10 10" aria-hidden="true"><path d="M2 0.5 L3.6 2.6 L2.7 3.6 Q3.8 5.9 6.4 7.3 L7.4 6.4 L9.5 8 L8.3 9.5 Q4.5 9.3 1.6 5.8 Q0.2 3.6 0.6 1.6 Z" fill="#8a8a8a"/></svg>
        833-555-2690
      </p>
    </div>
    <div class="agent-photo" role="img" aria-label="Portrait of Marcus Pellow in a navy suit jacket and light shirt"></div>
  </section>

  <section class="card card-back">
    <div class="back-brand">
      <div class="brand-mark" aria-hidden="true"></div>
      <p class="brand-name">The Harbor Crew</p>
      <p class="brand-sub">at Keystead Real Estate</p>
    </div>
  </section>
</body>
</html>
```